Design cd cover for the vocal group: Ember, cd title Harbor Light. Cd cover is for EP release to be followed by full album. Songs are: Sizwe Langa Khona(Lift high the lamp); Cold River Road; Ngolwazi(Guide me through the night); When Rain Falls. There is no track entitled harbor light; the concept of the sound of gospel music as embodied in the music tracks - contemporary and traditional - is the basis of the album title.
NB: Project can close Tuesday 12 November to account for the 5 days as I do not count Saturday as a working day.
Hey guys,
Hello to everyone. I would like to take this opportunity to say thank you for your participation. Your submissions have been great and much appreciated. Forgive me for not being able to provide feedback to all of you. The time has come for me to make selection decisions and I would like to say thank you to all for your participation, you have been great and amazing.

```html
<!DOCTYPE html>
<html lang="en">
<head>
<meta charset="utf-8">
<title>Harbor Light – Ember – Tracklist</title>
<link rel="stylesheet" href="https://fonts.googleapis.com/css2?family=Montserrat:wght@300;400&display=swap">
<style>
  :root {
    --sky-top: #3db0ba;
    --sky-mid: #2399a9;
    --sky-deep: #17748c;
    --sky-haze: rgba(150, 220, 225, 0.35);
    --cloud-light: #f6efe6;
    --cloud-blush: #e6c3cf;
    --track-text: #c4f2f1;
    --track-accent: #82e4ee;
  }
  html, body {
    margin: 0;
    padding: 0;
    width: 1200px;
    height: 1200px;
    overflow: hidden;
    background: var(--sky-mid);
  }
  .cover {
    position: relative;
    width: 1200px;
    height: 1200px;
    overflow: hidden;
    font-family: "Montserrat", "Helvetica Neue", Arial, sans-serif;
  }
  .sky-photo {
    position: absolute;
    inset: 0;
    background:
      radial-gradient(ellipse 720px 260px at 680px 1160px, var(--cloud-light) 0%, rgba(240, 225, 225, 0.85) 40%, rgba(230, 195, 207, 0) 100%),
      radial-gradient(ellipse 420px 200px at 1120px 1060px, var(--cloud-blush) 0%, rgba(230, 195, 207, 0) 100%),
      radial-gradient(ellipse 520px 360px at 200px 820px, var(--sky-haze) 0%, rgba(150, 220, 225, 0) 100%),
      radial-gradient(ellipse 700px 500px at 160px 1100px, rgba(23, 80, 120, 0.55) 0%, rgba(23, 80, 120, 0) 100%),
      linear-gradient(165deg, var(--sky-top) 0%, var(--sky-mid) 45%, var(--sky-deep) 100%);
  }
  .tracklist-block {
    position: absolute;
    left: 177px;
    top: 265px;
    color: var(--track-text);
    font-weight: 300;
    text-transform: uppercase;
  }
  .release-credit {
    margin: 0 0 22px;
    font-size: 26px;
    letter-spacing: 0.2em;
    color: var(--track-accent);
    white-space: nowrap;
  }
  .tracklist {
    margin: 0;
    padding: 0;
    list-style: none;
    font-size: 37px;
    letter-spacing: 0.08em;
  }
  .track {
    display: flex;
    height: 72px;
    align-items: center;
    white-space: nowrap;
  }
  .track-number {
    width: 93px;
    flex: none;
  }
  .track-version-accent {
    color: var(--track-accent);
  }
</style>
</head>
<body>
  <main class="cover">
    <div class="sky-photo" role="img" aria-label="Photograph of a bright teal sky with sun rays and white clouds along the bottom edge"></div>
    <section class="tracklist-block">
      <p class="release-credit">Ember · Harbor Light</p>
      <ol class="tracklist">
        <li class="track"><span class="track-number">1:</span><span class="track-title">Sizwe Langa Khona</span></li>
        <li class="track"><span class="track-number">2:</span><span class="track-title">Cold River Road</span></li>
        <li class="track"><span class="track-number">3:</span><span class="track-title">Ngolwazi</span></li>
        <li class="track"><span class="track-number">4:</span><span class="track-title">When Rain Falls</span></li>
        <li class="track"><span class="track-number">5:</span><span class="track-title">Sizwe Langa Khona (Original Cut)</span></li>
        <li class="track"><span class="track-number">6:</span><span class="track-title">Ngolwazi <span class="track-version-accent">(Original Cut)</span></span></li>
      </ol>
    </section>
  </main>
</body>
</html>
```